PowerPoint Template

We would like new powerpoint template for our organization: Fjordvik Data Guild.
Enclosed you find our logo and old template.
Industry/Entity Type
Computer
Requirements
Must have
- 1. Logo
2. Footer (for autor)
3. Font: Variations of ARIAL

```html
<!DOCTYPE html>
<html lang="en">
<head>
<meta charset="utf-8">
<title>Fjordvik Data Guild – hvem vi er</title>
<link rel="stylesheet" href="https://fonts.googleapis.com/css2?family=Open+Sans:wght@300;400&family=Roboto:wght@100;300&display=swap">
<style>
  :root {
    --page-bg: #ffffff;
    --text-body: #6a6a6a;
    --text-title: #3a3a3a;
    --band-start: #efefef;
    --band-line: #e6e6e6;
    --footer-bg: #135a80;
    --footer-link: #2f86b3;
    --footer-text: #c9dbe6;
    --brand-square: #e8413f;
    --brand-text: #2a2a2a;
    --photo-light: #eef1f4;
    --photo-mid: #c9ccd0;
    --photo-warm: #d9b9a3;
  }
  * { margin: 0; padding: 0; box-sizing: border-box; }
  html, body { width: 1200px; height: 656px; overflow: hidden; background: var(--page-bg); }
  body { position: relative; font-family: "Open Sans", Arial, sans-serif; color: var(--text-body); }

  .brand {
    position: absolute; left: 201px; top: 40px; width: 120px;
    display: flex; align-items: flex-start; gap: 8px;
  }
  .brand-square { width: 22px; height: 22px; background: var(--brand-square); flex: none; margin-top: 3px; }
  .brand-name {
    font-family: "Open Sans", Arial, sans-serif; font-weight: 400;
    font-size: 17px; line-height: 22px; color: var(--brand-text);
  }

  .title-band {
    position: absolute; left: 378px; top: 73px; width: 621px; height: 65px;
    background: linear-gradient(to right, var(--band-start), var(--page-bg) 60%);
    border-top: 1px solid var(--band-line); border-bottom: 1px solid var(--band-line);
  }
  .slide-title {
    position: absolute; right: 6px; top: 2px;
    font-family: "Roboto", Arial, sans-serif; font-weight: 100;
    font-size: 46px; line-height: 56px; color: var(--text-title); letter-spacing: 0.5px;
  }

  .photo {
    position: absolute; left: 201px; top: 238px; width: 385px; height: 146px;
    background: linear-gradient(160deg, var(--photo-light) 0%, var(--photo-mid) 45%, var(--photo-warm) 75%, var(--photo-mid) 100%);
  }

  .intro, .details {
    position: absolute; font-size: 15px; line-height: 22px; font-weight: 400; text-align: justify;
  }
  .intro { left: 625px; top: 251px; width: 374px; }
  .details { left: 201px; top: 409px; width: 798px; text-align: left; }

  .rights {
    position: absolute; left: 1171px; top: 588px; transform-origin: 0 0; transform: rotate(-90deg);
    font-size: 7px; color: #333; white-space: nowrap; width: 150px; text-align: center;
  }

  .footer {
    position: absolute; left: 0; top: 598px; width: 1200px; height: 58px; background: var(--footer-bg);
  }
  .nav { position: absolute; top: 18px; display: flex; align-items: center; gap: 4px; font-size: 12px; color: var(--footer-link); }
  .nav-prev { left: 201px; }
  .nav-next { right: 201px; }
  .nav svg { display: block; }
  .author { position: absolute; left: 0; width: 100%; top: 21px; text-align: center; font-size: 12px; color: var(--footer-text); }
</style>
</head>
<body>
  <div class="brand">
    <span class="brand-square"></span>
    <span class="brand-name">Fjordvik Data Guild</span>
  </div>

  <header class="title-band">
    <h1 class="slide-title">hvem vi er</h1>
  </header>

  <div class="photo" role="img" aria-label="Photo of a hand touching a tablet screen"></div>

  <p class="intro">The FDG is the largest special interest society for information technology (IT) in Norway. It is an open, independent forum for Norway's IT professionals and advanced IT users. The society encompasses the IT industry, corporations in general and research and development institutions.</p>

  <p class="details">The FDG is an independent and wholly self-financed society with more than 10,500 registered members and more than 1,200 company members.</p>

  <div class="rights">fjordvikdata.no - 2014, all rights reserved</div>

  <footer class="footer">
    <div class="nav nav-prev">
      <svg width="12" height="26" viewBox="0 0 12 26"><polyline points="11,1 2,13 11,25" fill="none" stroke="currentColor" stroke-width="2"/></svg>
      <span>Previous</span>
    </div>
    <div class="author">Presentation by: Mr. Erik N Holm</div>
    <div class="nav nav-next">
      <span>Next</span>
      <svg width="12" height="26" viewBox="0 0 12 26"><polyline points="1,1 10,13 1,25" fill="none" stroke="currentColor" stroke-width="2"/></svg>
    </div>
  </footer>
</body>
</html>
```